Skillet Sam food truck needs a flashy design for vinyl vehicle wrap.

Background: we are a new concept food truck serving high quality gourmet style burgers and burritos.

What we need:
a modern and funky design based on and using our logo and colour schemes. Black red yellow.

The background should be either yellow or white.

The vinyl wrap will cover the whole vehicle. Designs must take into account position of windows and door of the vehicle.

An accrylic logo will be positioned between the door and window on the side of vehicle. Another accrylic logo will be positioned on the other side of vehicle in the middle.

The dimensions of vehicle:
Sides: 7.3 M x 2.3 M
Front: 2.3 M x 2.3 M

Requirements
Must have
• room for the acrylic logo on the service side in between the window and door of vehicle. and on the other side preferably the middle. therefore overall design should integrate this and have a nice flow.
Nice to have
• menu items: burritos, burgers, buffalo ribs, waffles.

```html
<!DOCTYPE html>
<html lang="en">
<head>
<meta charset="utf-8">
<title>Skillet Sam – Vehicle Wrap Side</title>
<link href="https://fonts.googleapis.com/css2?family=Permanent+Marker&family=Kaushan+Script&family=Oswald:wght@500&display=swap" rel="stylesheet">
<style>
  :root {
    --yellow: #ffc20e;
    --yellow-light: #ffd430;
    --orange: #f7941d;
    --orange-deep: #ec6a12;
    --red: #c8281e;
    --wine: #8e1526;
    --black: #111111;
    --white: #ffffff;
    --page: #ffffff;
  }
  * { box-sizing: border-box; margin: 0; padding: 0; }
  html, body { width: 1200px; height: 1000px; overflow: hidden; background: var(--page); }
  .canvas { position: relative; width: 1200px; height: 1000px; }

  .wrap-side {
    position: absolute; left: 46px; top: 321px; width: 1108px; height: 358px;
    overflow: hidden;
    background:
      radial-gradient(ellipse 380px 200px at 0% 0%, var(--orange-deep) 0%, rgba(236,106,18,0) 100%),
      radial-gradient(ellipse 300px 120px at 100% 0%, var(--orange-deep) 0%, rgba(236,106,18,0) 100%),
      linear-gradient(180deg, var(--orange) 0%, var(--yellow) 30%, var(--yellow-light) 60%, var(--orange) 100%);
  }
  .wrap-side .swoosh { position: absolute; inset: 0; width: 100%; height: 100%; }

  .hero-illustration {
    position: absolute; left: 58px; top: 18px; width: 150px; height: 304px;
    border-radius: 40px 40px 70px 70px;
    background: linear-gradient(180deg, #bfbfbf 0%, #d9d2b8 45%, #c98a3a 70%, #8a4a20 100%);
  }

  .menu-list {
    position: absolute; left: 240px; top: 62px; width: 120px;
    list-style: none; text-align: center;
    font-family: "Permanent Marker", cursive; color: var(--wine);
    font-size: 14px; line-height: 1.05;
  }
  .menu-list li { margin-bottom: 27px; }

  .brand {
    position: absolute; left: 395px; top: 62px; width: 210px; height: 100px;
    display: flex; align-items: center; justify-content: center; gap: 10px;
  }
  .brand-dot { width: 58px; height: 58px; border-radius: 50%; background: var(--red); flex: none; }
  .brand-name {
    font-family: "Permanent Marker", cursive; font-size: 34px; color: var(--black);
    white-space: nowrap;
  }
  .brand-web {
    position: absolute; left: 395px; top: 164px; width: 210px; text-align: center;
    font-family: "Permanent Marker", cursive; font-size: 11px; color: var(--black);
  }

  .slogan {
    position: absolute; left: 660px; top: 86px; width: 410px; text-align: center;
    font-family: "Kaushan Script", cursive; font-size: 44px; color: var(--black);
    white-space: nowrap;
  }

  .social {
    position: absolute; left: 676px; top: 214px;
    display: flex; align-items: center; gap: 8px;
    font-family: "Permanent Marker", cursive; font-size: 9.5px; color: var(--black);
  }
  .social .follow { color: var(--wine); font-size: 11px; margin-right: 8px; }
  .social .mark { width: 14px; height: 14px; background: #3b4a8c; flex: none; }
  .social .mark.alt { background: #5a4636; margin-left: 40px; }

  .tagline-band {
    position: absolute; left: 0; top: 258px; width: 1108px; height: 38px;
    background: var(--black);
  }
  .tagline {
    position: absolute; right: 30px; top: 258px; height: 38px; line-height: 40px;
    font-family: "Permanent Marker", cursive; font-size: 27px; color: var(--white);
    letter-spacing: 0.5px; white-space: nowrap;
  }
</style>
</head>
<body>
<main class="canvas">
  <section class="wrap-side">
    <svg class="swoosh" viewBox="0 0 1108 358" preserveAspectRatio="none" aria-hidden="true">
      <path d="M560 258 C760 200 950 170 1108 95 L1108 258 Z" fill="var(--orange-deep)" opacity="0.55"/>
      <path d="M0 300 C300 330 700 290 1108 330 L1108 358 L0 358 Z" fill="var(--orange-deep)" opacity="0.6"/>
      <path d="M0 296 C260 310 600 320 1108 300 L1108 318 C700 336 300 330 0 320 Z" fill="var(--yellow)" opacity="0.6"/>
    </svg>

    <div class="hero-illustration" role="img" aria-label="Illustration of a katana skewering a chicken wing, a burrito and a stacked burger"></div>

    <ul class="menu-list">
      <li>BURRITOS</li>
      <li>BURGERS</li>
      <li>BUFFALO<br>CHICKEN RIBS</li>
      <li>BELGIAN<br>WAFFLES</li>
    </ul>

    <div class="brand">
      <span class="brand-dot"></span>
      <span class="brand-name">Skillet Sam</span>
    </div>
    <p class="brand-web">WWW.SKILLETSAM.COM.AU</p>

    <p class="slogan">streetfood master</p>

    <div class="social">
      <span class="follow">FOLLOW US:</span>
      <span class="mark"></span>
      <span>/SKILLETSAM.STREETFOOD</span>
      <span class="mark alt"></span>
      <span>@SKILLETSAM.EATS</span>
    </div>

    <div class="tagline-band"></div>
    <p class="tagline">“STREET FOOD IS A DISH BEST SERVED GRILLED”</p>
  </section>
</main>
</body>
</html>
```